One pager Business Profile BrightHire

We would like to create a onepage with our company profile. It is important to keep the basis like it is in the word document but make it nice and fancy. Consistancy in color and fonts is important.

I've added the logo so you can pick the correct colors. The small logo's you can reuse, I want to replace them once you are ready.

In the word document we used standard Word stuff, I would like nice symbols and a professional well designed block in the Cooperation part

I would like to have a source file so I can change (and translate) text, so better to use a regular font or free font (I need the font than).

Target Market(s)

Recruitment

Industry/Entity Type

Recruitment

Requirements
Must have
• a professional look

```html
<!DOCTYPE html>
<html lang="en">
<head>
<meta charset="utf-8">
<title>BrightHire – Business Profile</title>
<link rel="stylesheet" href="https://fonts.googleapis.com/css2?family=Montserrat:ital,wght@0,500;0,600;0,700;1,700&family=Sorts+Mill+Goudy:ital@0;1&display=swap">
<style>
:root{
  --navy:#275a85;
  --sky:#85c1f8;
  --ink:#214d7d;
  --brand:#1b74bb;
  --charcoal:#4a4a4c;
  --gold:#c6a933;
  --gold-soft:#dcc879;
  --gold-pale:#e4d8a2;
  --slate:#959ca5;
  --coral:#f46a50;
  --mist:#d6dde5;
  --white:#fff;
}
*{margin:0;padding:0;box-sizing:border-box}
html,body{width:848px;height:1200px;overflow:hidden;background:var(--white)}
.page{position:relative;width:848px;height:1200px;overflow:hidden;font-family:"Sorts Mill Goudy",Georgia,serif;color:var(--ink)}
.abs{position:absolute}
.brand{top:16px;left:0;width:848px;text-align:center;font-family:"Montserrat",sans-serif;font-weight:700;font-size:56px;letter-spacing:16px;color:var(--brand);line-height:60px;padding-left:16px}
.tagline{top:77px;left:0;width:848px;text-align:center;font-family:"Montserrat",sans-serif;font-weight:500;font-size:14px;color:var(--ink)}
.quote-band{top:111px;left:0;width:848px;height:47px;background:var(--navy);color:var(--white);font-style:italic;font-size:21px;text-align:center;line-height:47px}
.years{top:163px;left:50px;width:200px;height:110px}
.network{top:183px;left:262px;width:520px;text-align:center;font-family:"Montserrat",sans-serif;font-weight:700;font-style:italic;font-size:19px;line-height:24px;color:var(--ink)}
.banner{position:absolute;height:52px}
.banner .back{position:absolute;inset:8px -6px -8px 0;background:var(--sky)}
.banner .front{position:absolute;inset:0;background:var(--navy);color:var(--white);font-family:"Montserrat",sans-serif;font-weight:700;font-size:24px;letter-spacing:.5px;display:flex;align-items:center}
.banner.left .back,.banner.left .front{clip-path:polygon(0 0,100% 0,calc(100% - 22px) 100%,0 100%)}
.banner.right .back,.banner.right .front{clip-path:polygon(0 0,100% 0,100% 100%,26px 100%)}
.body-text{font-size:18.5px;line-height:24px;color:var(--ink)}
.teams-box{top:283px;left:468px;width:348px;height:242px}
.teams-box .shade{position:absolute;left:13px;top:11px;width:348px;height:242px;background:var(--sky)}
.teams-box .panel{position:absolute;inset:0;background:var(--navy);color:var(--white);font-style:italic;font-size:22px;line-height:27.5px;padding:22px 16px 0 32px}
.expertise{top:634px;left:488px;width:360px;font-size:16.5px;line-height:20.5px;color:var(--ink)}
.stars{display:flex;gap:22px;padding-left:44px}
.logo-cluster{top:1030px;left:34px;width:385px;height:135px}
.coop{top:925px;left:500px;width:330px;height:222px}
.vert{position:absolute;font-family:"Montserrat",sans-serif;font-weight:600;font-size:12px;color:var(--charcoal);writing-mode:vertical-rl;text-orientation:upright;letter-spacing:1.5px}
.cell{position:absolute;display:flex;align-items:center;justify-content:center;text-align:center;font-family:"Montserrat",sans-serif;font-weight:700;line-height:16px}
.footer-band{top:1180px;left:0;width:848px;height:20px;background:var(--brand)}
</style>
</head>
<body>
<div class="page">

  <div class="abs brand">BRIGHTHIRE</div>
  <div class="abs tagline">Better experts, faster The best developers in our network</div>

  <div class="abs quote-band">“We offer our professionals only if we are convinced&nbsp; of their competences and skills"</div>

  <svg class="abs years" viewBox="0 0 200 110" aria-label="15 years">
    <circle cx="25" cy="76" r="24" fill="var(--gold-pale)"/>
    <circle cx="60" cy="70" r="32" fill="var(--gold-soft)" opacity=".75"/>
    <circle cx="140" cy="55" r="55" fill="var(--gold)"/>
    <text x="136" y="80" text-anchor="middle" font-family="Sorts Mill Goudy, serif" font-style="italic" font-size="66" fill="var(--white)">15</text>
  </svg>
  <div class="abs network">We have access to a specialist network of software development professionals carefully built up<br>over a period of 15 years</div>

  <div class="banner left" style="top:287px;left:0;width:265px">
    <div class="back"></div><div class="front" style="padding-left:29px">OUR OFFER</div>
  </div>
  <p class="abs body-text" style="top:360px;left:29px;width:370px">BrightHire helps you solve your IT organisation's capacity problems by offering and deploying high-quality, highly develope candidates.<br>Our candidates, our professionals, are driven, and they are used to getting the best out of themselves and their project. They bring up-to-date knowledge for you, so they immediately tap the best level for you as a client to help achieve the objectives of the project, and therefore really complement your team. Our professionals are of immediate value and deliver demonstrable results..</p>

  <div class="abs teams-box">
    <div class="shade"></div>
    <div class="panel">As part of the ClearPath Group and our partner network, BrightHire is able to provide clients with full development teams, complete with test automators, scrum masters, product owners and business</div>
  </div>

  <div class="banner right" style="top:555px;left:463px;width:385px">
    <div class="back" style="inset:8px 0 -8px 8px"></div><div class="front" style="padding-left:62px">TEAM EXPERTISES</div>
  </div>
  <div class="abs expertise">
    Backend developers<br>
    Frontend developers (web frameworks)<br>
    Core developers Data engineers Devops<br>
    (cloud platforms) Web developers<br>
    Testers (automation &amp; functioneel)<br>
    Mobile developers (phone / tablet)<br>
    UX/UI developers<br>
    BrightHire&nbsp; | Lindenlaan 24 |1234 AB Veenhoven<br>
    0031 10 555 0192&nbsp; |&nbsp; info@brighthire.example
  </div>

  <div class="banner left" style="top:692px;left:0;width:242px">
    <div class="back"></div>
    <div class="front">
      <div class="stars">
        <svg width="38" height="36" viewBox="0 0 24 23"><path d="M12 0l2.8 8.3H24l-7.3 5.4 2.8 8.8L12 17.1l-7.5 5.4 2.8-8.8L0 8.3h9.2z" fill="var(--white)"/></svg>
        <svg width="38" height="36" viewBox="0 0 24 23"><path d="M12 0l2.8 8.3H24l-7.3 5.4 2.8 8.8L12 17.1l-7.5 5.4 2.8-8.8L0 8.3h9.2z" fill="var(--white)"/></svg>
        <svg width="38" height="36" viewBox="0 0 24 23"><path d="M12 0l2.8 8.3H24l-7.3 5.4 2.8 8.8L12 17.1l-7.5 5.4 2.8-8.8L0 8.3h9.2z" fill="var(--white)"/></svg>
      </div>
    </div>
  </div>
  <p class="abs body-text" style="top:759px;left:30px;width:385px">By employing qualitatively suitable candidates, we receive positive customer reviews and score high customer satisfaction.</p>

  <div class="banner left" style="top:850px;left:0;width:415px">
    <div class="back"></div><div class="front" style="padding-left:30px">TRANSPARENCY &amp; OPEN</div>
  </div>
  <p class="abs body-text" style="top:921px;left:29px;width:450px">BrightHire stands for transparency and openness, for both client and contractor. Clear agreements and no unnecessary obligations.Short lines, and smooth response times. For both the client and the professional.</p>

  <svg class="abs logo-cluster" viewBox="0 0 385 135" role="img" aria-label="Client badges">
    <circle cx="30" cy="55" r="22" fill="var(--sky)"/>
    <circle cx="80" cy="28" r="24" fill="var(--navy)"/>
    <circle cx="78" cy="85" r="22" fill="var(--mist)"/>
    <circle cx="132" cy="30" r="19" fill="var(--gold-soft)"/>
    <circle cx="124" cy="72" r="17" fill="var(--brand)"/>
    <circle cx="160" cy="100" r="14" fill="var(--slate)"/>
    <circle cx="190" cy="28" r="25" fill="var(--navy)"/>
    <circle cx="172" cy="64" r="13" fill="var(--sky)"/>
    <circle cx="128" cy="112" r="11" fill="var(--gold-pale)"/>
    <rect x="192" y="78" width="28" height="26" rx="4" fill="var(--mist)"/>
    <rect x="182" y="108" width="56" height="24" rx="2" fill="var(--navy)"/>
    <circle cx="236" cy="58" r="15" fill="var(--brand)"/>
    <circle cx="250" cy="22" r="18" fill="var(--sky)"/>
    <circle cx="262" cy="92" r="16" fill="var(--slate)"/>
    <circle cx="300" cy="30" r="24" fill="var(--brand)"/>
    <circle cx="310" cy="90" r="24" fill="var(--navy)"/>
    <circle cx="282" cy="62" r="11" fill="var(--gold-soft)"/>
    <circle cx="355" cy="58" r="21" fill="var(--sky)"/>
  </svg>

  <div class="banner right" style="top:850px;left:505px;width:343px">
    <div class="back" style="inset:8px 0 -8px 8px"></div><div class="front" style="padding-left:50px">COOPERATION</div>
  </div>

  <div class="abs coop">
    <svg class="abs" style="left:0;top:0" width="330" height="222" viewBox="0 0 330 222" aria-hidden="true">
      <g stroke="var(--charcoal)" stroke-width="1.3" fill="var(--charcoal)">
        <line x1="38" y1="4" x2="38" y2="218"/>
        <path d="M35 8l3-7 3 7z"/><path d="M35 214l3 7 3-7z"/>
        <line x1="286" y1="4" x2="286" y2="218"/>
        <path d="M283 8l3-7 3 7z"/><path d="M283 214l3 7 3-7z"/>
      </g>
    </svg>
    <div class="vert" style="left:0;top:18px">CUSTOMER</div>
    <div class="vert" style="left:15px;top:88px">REQUEST</div>
    <div class="vert" style="left:295px;top:18px">CUSTOMER</div>
    <div class="vert" style="left:310px;top:88px">REQUEST</div>

    <div class="cell" style="left:46px;top:2px;width:73px;height:84px;background:var(--slate);color:var(--brand);font-size:12.5px">CLEAR<br>PATH<br>GROUP</div>
    <div class="cell" style="left:125px;top:2px;width:73px;height:84px;background:var(--sky);color:var(--brand);font-size:12px">NETWERK<br>PARTIJEN</div>
    <div class="cell" style="left:204px;top:2px;width:73px;height:84px;background:var(--coral);color:var(--brand);font-size:12.5px">KLANT</div>
    <div class="cell" style="left:47px;top:91px;width:230px;height:91px;background:var(--brand);color:var(--white);font-size:15.5px">BRIGHTHIRE</div>
    <div class="cell" style="left:47px;top:186px;width:230px;height:34px;background:var(--brand);color:var(--white);font-size:14px">ZZP’ers / DEVELOPERS</div>
  </div>

  <div class="abs footer-band"></div>
</div>
</body>
</html>
```